Social Media Graphics - Copperfield Loop

Create 6-7 individual social media graphics (square size) to encourage folks to join our online course, using either of the text below (only one set of text per graphic:

The Lantern Ridge Method
How to Create a 7-Figure Business From Scratch
Sign Up Today!

Or

The Lantern Ridge Method
Fast-track Your Way to a Multi-Million Business!
Sign Up Today!

For the color scheme of the graphics, use 1 or 2 colors in the color palette attached; or use any colors that look nice with their outfits; AVOID using red, white and blue altogether because it will look like an Independence Day (4th of July) graphic and we don’t want that; make sure the graphics appeal to both men and women

Make sure each graphic contains 1 of the 2 pics attached; and make sure one of the graphics is all TEXT only.

Target Market(s)

men and women looking to make more money

Industry/Entity Type

entrepreneurship

Requirements
Must have
• see the text document attached
Nice to have
• We are open to a nice color design; the color palette colors are not required, especially we don't want red, white and blue used together
Should not have
• AVOID using red, white and blue altogether because it will look like an Independence Day (4th of July) graphic and we dont want that

```html
<!DOCTYPE html>
<html lang="en">
<head>
<meta charset="utf-8">
<title>The Lantern Ridge Method – Sign Up Today</title>
<link rel="stylesheet" href="https://fonts.googleapis.com/css2?family=Anton&family=Archivo:wdth,wght@125,900&family=Bebas+Neue&display=swap">
<style>
  :root {
    --ink: #1f1528;
    --berry: #8c1d57;
    --blush: #f3b5c9;
    --cream: #fff6ea;
    --gold: #e0b04a;
    --photo-rose: #d9577f;
    --photo-deep: #3a2430;
  }
  html, body {
    margin: 0;
    padding: 0;
    width: 1200px;
    height: 1200px;
    overflow: hidden;
    background: var(--ink);
  }
  .poster {
    display: block;
    width: 1200px;
    height: 1200px;
  }
  .bg-base { fill: var(--ink); }
  .bg-shield { fill: var(--berry); }
  .bg-blush { fill: var(--blush); }
  .title-band { fill: var(--ink); }
  .title-small {
    font-family: "Archivo", "Arial Black", sans-serif;
    font-weight: 900;
    font-stretch: 125%;
    font-size: 80px;
    fill: var(--cream);
  }
  .title-large {
    font-family: "Anton", "Impact", sans-serif;
    font-size: 205px;
    fill: var(--cream);
  }
  .tagline {
    font-family: "Bebas Neue", "Oswald", sans-serif;
    font-size: 72px;
    fill: var(--cream);
  }
  .cta {
    font-family: "Archivo", "Arial Black", sans-serif;
    font-weight: 900;
    font-stretch: 125%;
    font-size: 40px;
    fill: var(--gold);
  }
</style>
</head>
<body>
<svg class="poster" viewBox="0 0 1200 1200" xmlns="http://www.w3.org/2000/svg">
  <defs>
    <linearGradient id="hostsTone" x1="0" y1="0" x2="1" y2="0.3">
      <stop offset="0" stop-color="var(--photo-rose)"/>
      <stop offset="0.5" stop-color="#a4406a"/>
      <stop offset="1" stop-color="var(--photo-deep)"/>
    </linearGradient>
  </defs>

  <rect class="bg-base" x="0" y="0" width="1200" height="1200"/>
  <path class="bg-shield" d="M0 0 H793 C800 140 770 260 715 350 C600 560 420 850 166 1048 L0 882 Z"/>
  <path class="bg-blush" d="M410 1037 C395 860 470 640 640 520 C780 430 900 400 1010 405 C1090 410 1150 430 1200 460 V1037 Z"/>

  <rect role="img" aria-label="Photo of the two course hosts standing side by side" fill="url(#hostsTone)" x="472" y="380" width="698" height="657" rx="36"/>

  <rect class="title-band" x="211" y="55" width="582" height="98"/>
  <text class="title-small" x="239" y="138" textLength="721" lengthAdjust="spacingAndGlyphs">THE LANTERN</text>

  <text class="title-large" x="78" y="351" textLength="1046" lengthAdjust="spacingAndGlyphs">RIDGE METHOD</text>

  <text class="tagline" x="81" y="475" textLength="285" lengthAdjust="spacingAndGlyphs">FAST-TRACK</text>
  <text class="tagline" x="81" y="603" textLength="368" lengthAdjust="spacingAndGlyphs">YOUR WAY TO A</text>
  <text class="tagline" x="81" y="733" textLength="358" lengthAdjust="spacingAndGlyphs">MULTI-MILLION</text>
  <text class="tagline" x="81" y="860" textLength="244" lengthAdjust="spacingAndGlyphs">BUSINESS!</text>

  <text class="cta" x="245" y="1141" textLength="708" lengthAdjust="spacingAndGlyphs">SIGN UP TODAY!</text>
</svg>
</body>
</html>
```